Milo Castell Moving DL Flyer

We need a double sided DL flyer to give to patients to let them know that we are moving location.
On one side we would like it to read:
"We Are Moving!" and "November 2017" and our logo.
On the other side we would like it to read:
"Same Great Staff"
"Same Great Service"
"Bigger, Brighter and Better"
"New Location at 42 Quarry Rd"
with a map below (attached)
The flyer should follow our practice branding. Attached is a copy of our business card as an example of this.

```html
<!DOCTYPE html>
<html lang="en">
<head>
<meta charset="utf-8">
<title>Milo Castell Optometry – Moving DL Flyer</title>
<link href="https://fonts.googleapis.com/css2?family=Source+Sans+3:wght@300;400;600&display=swap" rel="stylesheet">
<style>
  :root {
    --plum: #4b3a52;
    --plum-deep: #3f3046;
    --red: #c8141b;
    --paper: #f4f4f5;
    --paper-shade: #dcdcde;
    --white: #ffffff;
    --backdrop: #ece8e3;
    --cart-box: #b98a5e;
    --cart-frame: #d23a34;
    --map-road: #2a2a2a;
    --map-ground: #bdbdbd;
  }
  * { box-sizing: border-box; margin: 0; padding: 0; }
  html, body { width: 1200px; height: 889px; overflow: hidden; }
  body {
    background: var(--backdrop);
    font-family: "Source Sans 3", "Helvetica Neue", Arial, sans-serif;
    position: relative;
  }

  /* Front side */
  .flyer-front {
    position: absolute;
    left: 130px; top: 330px;
    width: 580px; height: 270px;
    background: linear-gradient(180deg, var(--white) 0%, var(--paper) 60%, var(--paper-shade) 100%);
    box-shadow: 0 4px 10px rgba(0,0,0,.25);
  }
  .hand-truck-art {
    position: absolute;
    left: 50px; top: 30px;
    width: 190px; height: 220px;
    border-radius: 6px;
    background: linear-gradient(160deg, var(--cart-frame) 0%, var(--cart-box) 35%, #a87a50 75%, #555 100%);
    opacity: .85;
  }
  .moving-heading {
    position: absolute;
    left: 260px; top: 58px; width: 300px;
    text-align: center;
    font-weight: 400;
    font-size: 30px;
    color: var(--plum);
  }
  .moving-date {
    position: absolute;
    left: 245px; top: 92px; width: 330px;
    text-align: center;
    font-weight: 400;
    font-size: 46px;
    color: var(--red);
    letter-spacing: -.5px;
  }
  .date-rule {
    position: absolute;
    left: 255px; top: 150px;
    width: 310px; height: 6px;
    background: var(--plum);
  }
  .practice-name {
    position: absolute;
    left: 260px; top: 188px; width: 300px;
    display: flex; align-items: center; justify-content: center; gap: 10px;
    font-weight: 600;
    font-size: 24px;
    color: var(--plum);
  }
  .practice-name .mark {
    width: 14px; height: 14px; border-radius: 50%;
    background: var(--plum);
  }

  /* Back side */
  .flyer-back {
    position: absolute;
    left: 770px; top: 140px;
    width: 290px; height: 600px;
    background: var(--plum);
    box-shadow: 0 4px 10px rgba(0,0,0,.25);
    color: var(--white);
    text-align: center;
  }
  .promise {
    position: absolute; top: 30px; left: 0; width: 100%;
    font-size: 12px; font-weight: 400;
  }
  .headline-rule {
    position: absolute; left: 20px; width: 250px; height: 2px;
    background: var(--white);
  }
  .headline-rule.top { top: 72px; }
  .headline-rule.bottom { top: 170px; }
  .headline {
    position: absolute; top: 82px; left: 0; width: 100%;
    font-size: 31px; font-weight: 400; line-height: 1.2;
  }
  .location-label {
    position: absolute; top: 200px; left: 0; width: 100%;
    font-size: 15px; font-weight: 400;
  }
  .address-box {
    position: absolute; top: 232px; left: 48px;
    width: 194px; height: 52px;
    border: 2px solid var(--white);
    font-size: 22px; line-height: 48px; font-weight: 400;
  }
  .pointer {
    position: absolute; top: 288px; left: 133px;
  }
  .map-frame {
    position: absolute; top: 340px; left: 25px;
    width: 240px; height: 230px;
    background: var(--white);
    padding: 8px;
  }
  .map-area {
    width: 100%; height: 100%;
    background: linear-gradient(135deg, var(--map-ground) 0%, #c9b8c4 45%, #d98a8a 70%, var(--map-road) 100%);
  }
</style>
</head>
<body>

<section class="flyer-front">
  <div class="hand-truck-art" role="img" aria-label="Illustration of a red hand truck carrying two cardboard moving boxes"></div>
  <h1 class="moving-heading">We Are Moving!</h1>
  <p class="moving-date">November 2017</p>
  <div class="date-rule"></div>
  <p class="practice-name"><span class="mark"></span>Milo Castell Optometry</p>
</section>

<section class="flyer-back">
  <p class="promise">Same Great Staff &nbsp;|&nbsp; Same Great Service</p>
  <div class="headline-rule top"></div>
  <h2 class="headline">Bigger, Brighter<br>and Better</h2>
  <div class="headline-rule bottom"></div>
  <p class="location-label">New Location at</p>
  <p class="address-box">42 Quarry Rd</p>
  <svg class="pointer" width="24" height="36" viewBox="0 0 24 36" aria-hidden="true">
    <rect x="9" y="0" width="6" height="20" fill="#ffffff"/>
    <polygon points="0,18 24,18 12,34" fill="#ffffff"/>
  </svg>
  <div class="map-frame">
    <div class="map-area" role="img" aria-label="Street map showing the new practice location beside the marketplace and car parking"></div>
  </div>
</section>

</body>
</html>
```